Unique Beautiful Realtor business card

I need a unique business card that includes my logo, my firms logo, my picture and phone number. The colors should compliment my logo.

Target Market(s)

People who want to buy or sell a home in South Florida

Contact Information for Business Card

Use two sides and work with the DRM Coastal Homes logo as a theme.
The Harlow Benton should be small and discreet, it is a requirement to be there but should be small. My photo should be integrated artistically.

Font styles to use
Serif
Sans Serif

Colors

Designer to choose colors to be used in the design.

Requirements
Must have
• My logo, Harlow Benton logo, my photo, my phone number, (954-283-6091) and my website address. (www.drmcoastalhomes.example)
• Also my name, Dana R. Moreland, PA, Realtor
• Also “Your Coastal Home Realtor”

```html
<!DOCTYPE html>
<html lang="en">
<head>
<meta charset="utf-8">
<title>Dana R. Moreland – Business Card</title>
<link rel="stylesheet" href="https://fonts.googleapis.com/css2?family=Open+Sans:wght@400;600;700;800&display=swap">
<style>
  :root {
    --sun-yellow: #fdd20e;
    --stripe-red: #be2035;
    --ocean-blue: #1b4a86;
    --card-white: #ffffff;
    --ink: #111111;
    --muted: #6d6d6d;
    --page: #f2f2f2;
  }
  * { box-sizing: border-box; margin: 0; padding: 0; }
  html, body { width: 1200px; height: 1200px; overflow: hidden; background: var(--page); }
  body { font-family: "Open Sans", Arial, sans-serif; position: relative; }

  .card {
    position: absolute;
    left: 150px;
    width: 900px;
    height: 500px;
    background: var(--card-white);
    box-shadow: 0 10px 30px rgba(0,0,0,0.18);
    overflow: hidden;
  }
  .card--front { top: 70px; }
  .card--back { top: 630px; }
  .card__bands { position: absolute; inset: 0; }

  .portrait {
    position: absolute;
    left: 105px; top: 79px;
    width: 238px; height: 238px;
    border-radius: 50%;
    border: 11px solid var(--ocean-blue);
    background: radial-gradient(circle at 50% 40%, #d9b98a 0%, #9c7a52 40%, #2f3442 75%, #1d2230 100%);
  }

  .agent { position: absolute; left: 76px; top: 342px; color: var(--ink); }
  .agent__name { font-weight: 800; font-size: 38px; line-height: 1.1; letter-spacing: 0.5px; }
  .agent__role { font-weight: 400; font-size: 25px; line-height: 1.35; letter-spacing: 1px; }

  .brand {
    position: absolute;
    display: flex; flex-direction: column; align-items: center;
    color: var(--ocean-blue);
    text-align: center;
  }
  .brand__mark { width: 46px; height: 46px; border-radius: 50%; background: var(--ocean-blue); margin-bottom: 10px; }
  .brand__name { font-weight: 800; line-height: 1.05; text-transform: uppercase; }
  .card--front .brand { left: 580px; top: 60px; width: 270px; }
  .card--front .brand__name { font-size: 30px; }
  .card--back .brand { left: 250px; top: 150px; width: 400px; }
  .card--back .brand__mark { width: 64px; height: 64px; margin-bottom: 16px; }
  .card--back .brand__name { font-size: 44px; }

  .firm {
    position: absolute; left: 580px; top: 236px; width: 270px;
    text-align: center; font-size: 15px; font-weight: 600;
    color: var(--muted); letter-spacing: 1px; text-transform: uppercase;
  }

  .contact { position: absolute; left: 540px; color: var(--ink); display: flex; align-items: center; gap: 10px; font-weight: 700; white-space: nowrap; }
  .contact svg { width: 26px; height: 26px; flex: none; }
  .contact--phone { top: 362px; font-size: 21px; letter-spacing: 6px; }
  .contact--web { top: 410px; font-size: 17px; letter-spacing: 0.3px; }
</style>
</head>
<body>

  <section class="card card--front" aria-label="Business card front">
    <svg class="card__bands" viewBox="0 0 900 500" aria-hidden="true">
      <rect x="0" y="0" width="517" height="500" fill="var(--sun-yellow)"/>
      <polygon points="435,0 480,0 502,500 487,500" fill="var(--stripe-red)"/>
      <polygon points="480,0 517,0 517,500 502,500" fill="var(--ocean-blue)"/>
    </svg>

    <div class="portrait" role="img" aria-label="Portrait photo of Dana R. Moreland"></div>

    <div class="agent">
      <p class="agent__name">Dana R. Moreland</p>
      <p class="agent__role">Your Coastal Home Realtor</p>
      <p class="agent__role">PA, Realtor</p>
    </div>

    <div class="brand">
      <span class="brand__mark"></span>
      <span class="brand__name">DRM Coastal Homes</span>
    </div>

    <p class="firm">Harlow Benton</p>

    <p class="contact contact--phone">
      <svg viewBox="0 0 26 26" aria-hidden="true">
        <circle cx="13" cy="13" r="13" fill="var(--ocean-blue)"/>
        <path d="M9 7.5c.6-.5 1.4-.4 1.8.2l1.2 1.9c.3.5.2 1.1-.2 1.5l-.8.7c.6 1.4 1.7 2.5 3.1 3.2l.7-.8c.4-.4 1-.5 1.5-.2l1.9 1.2c.6.4.7 1.2.2 1.8l-.9 1c-.7.7-1.800.9-2.700.5-3.100-1.400-5.500-3.800-6.900-6.900-.4-.9-.2-2 .5-2.700z" fill="#fff"/>
      </svg>
      954-283-6091
    </p>
    <p class="contact contact--web">
      <svg viewBox="0 0 26 26" aria-hidden="true">
        <circle cx="13" cy="13" r="13" fill="var(--ocean-blue)"/>
        <g fill="none" stroke="#fff" stroke-width="1.4">
          <circle cx="13" cy="13" r="6.5"/>
          <ellipse cx="13" cy="13" rx="2.8" ry="6.5"/>
          <line x1="6.5" y1="13" x2="19.5" y2="13"/>
        </g>
      </svg>
      www.drmcoastalhomes.example
    </p>
  </section>

  <section class="card card--back" aria-label="Business card back">
    <svg class="card__bands" viewBox="0 0 900 500" aria-hidden="true">
      <rect x="0" y="0" width="228" height="500" fill="var(--sun-yellow)"/>
      <polygon points="146,0 191,0 215,500 201,500" fill="var(--stripe-red)"/>
      <polygon points="191,0 228,0 228,500 215,500" fill="var(--ocean-blue)"/>
      <rect x="672" y="0" width="228" height="500" fill="var(--sun-yellow)"/>
      <polygon points="672,0 709,0 685,500 672,500" fill="var(--ocean-blue)"/>
      <polygon points="709,0 754,0 699,500 685,500" fill="var(--stripe-red)"/>
    </svg>

    <div class="brand">
      <span class="brand__mark"></span>
      <span class="brand__name">DRM Coastal Homes</span>
    </div>
  </section>

</body>
</html>
```